Business Card design for insurance broker in Denver, CO, USA

I need a business card designed using this logo that was just created. We sell life and disability income insurance to US consumers.
Looking for a professionally designed card to make use of the logo and have something to hand to prospects or new business referral sources. The card could be white, gray, black or whatever you would recommend.

Target Market(s)

US Consumers and other financial professionals that I partner with.

Industry/Entity Type

Insurance Broker

Contact Information for Business Card

Owen R. Tessler, CLU, LUTCF (please note that CLU should have a superscript R in a circle for registered trademark)
President
phone (555) 555-0147
email owen@brightlakecoverage.com
4620 W. Hollister Rd, Suite 310, Maple Ridge, CO 80999
Somewhere fit in a tagline saying "Your resource for life, long term care, and disability insurance" (maybe the back if it doesn't fit on the front, your call)

Font styles to use
Sans Serif

Requirements
Must have
• Must have logo in correct blue and gray colors, my name, address, phone, email. Order and placement determined by the designer.
• I just want something that looks a more professional than what I could have done using the business card designer tool on printmakerhub.com or CardNest, or any other do-it-yourself tool
• A regular rectangular business card with square corners is preferred
Nice to have
• I included the logos of 2 organizations I belong to (GQLF and BEPWO). They should be small, but visible on the back only. If it doesn’t look good, this is not a requirement, feel free to drop it.
Should not have
• Do not add any colors not already in the logo, except use of black and whites which are okay. If you use the logo on the back and want to make that in all black, gray or white, that may be okay as well.

```html
<!DOCTYPE html>
<html lang="en">
<head>
<meta charset="utf-8">
<title>Brightlake Coverage – Business Card</title>
<link rel="stylesheet" href="https://fonts.googleapis.com/css2?family=Montserrat:wght@700&family=Quicksand:wght@400;600;700&display=swap">
<style>
  :root {
    --brand-blue: #2380c4;
    --brand-gray: #9b9b9b;
    --card-white: #f7f7f7;
    --page-bg: #e6e8ea;
    --ink-white: #ffffff;
  }
  * { box-sizing: border-box; margin: 0; padding: 0; }
  html, body {
    width: 1200px; height: 900px; overflow: hidden;
    background: var(--page-bg);
    font-family: "Quicksand", sans-serif;
  }
  .sheet {
    width: 1200px; height: 900px;
    display: flex; flex-direction: column; align-items: center; justify-content: center;
    gap: 44px;
  }
  .card {
    position: relative;
    width: 630px; height: 360px;
    overflow: hidden;
    box-shadow: 0 6px 18px rgba(0,0,0,0.14);
  }

  /* Brand lockup */
  .brand { display: flex; align-items: center; gap: 14px; }
  .brand-dot { width: 30px; height: 30px; border-radius: 50%; flex: none; }
  .brand-name {
    font-family: "Montserrat", sans-serif; font-weight: 700;
    text-transform: uppercase; letter-spacing: 1px; line-height: 1;
    white-space: nowrap;
  }

  .tagline-strip {
    position: absolute; left: 0; right: 0; bottom: 0; height: 42px;
    background: var(--card-white);
    display: flex; align-items: center; justify-content: center;
    color: var(--brand-blue);
    font-size: 14px; font-weight: 600; letter-spacing: 3.2px;
    white-space: nowrap;
  }

  /* Back side */
  .card-back { background: var(--brand-blue); }
  .card-back .brand {
    position: absolute; left: 0; right: 0; top: 100px; justify-content: center;
  }
  .card-back .brand-dot { background: var(--ink-white); width: 40px; height: 40px; }
  .card-back .brand-name { color: var(--ink-white); font-size: 34px; }
  .card-back .back-email {
    position: absolute; left: 0; right: 0; top: 218px; text-align: center;
    color: var(--ink-white); font-size: 20px; letter-spacing: 2.5px; font-weight: 400;
  }

  /* Front side */
  .card-front { background: var(--card-white); }
  .card-front .brand { position: absolute; left: 30px; top: 34px; }
  .card-front .brand-dot { background: var(--brand-blue); }
  .card-front .brand-name { color: var(--brand-blue); font-size: 27px; }
  .memberships {
    position: absolute; right: 32px; top: 40px; display: flex; gap: 22px; align-items: center;
  }
  .person { position: absolute; left: 30px; top: 106px; }
  .person-name { color: var(--brand-blue); font-size: 28px; font-weight: 700; line-height: 1.1; }
  .person-title { color: var(--brand-gray); font-size: 18px; letter-spacing: 5px; font-weight: 400; line-height: 1.2; }
  .contact-band {
    position: absolute; left: 0; right: 0; top: 176px; bottom: 42px;
    background: var(--brand-blue);
    padding: 20px 30px 0;
    color: var(--ink-white); font-size: 19px; font-weight: 400; line-height: 1;
    display: flex; flex-direction: column; gap: 17px;
    white-space: nowrap;
  }
</style>
</head>
<body>
<main class="sheet">

  <section class="card card-back" aria-label="Card back">
    <div class="brand">
      <span class="brand-dot"></span>
      <span class="brand-name">Brightlake Coverage</span>
    </div>
    <p class="back-email">owen@brightlakecoverage.com</p>
    <p class="tagline-strip">Your resource for life, long term care, and disability insurance</p>
  </section>

  <section class="card card-front" aria-label="Card front">
    <div class="brand">
      <span class="brand-dot"></span>
      <span class="brand-name">Brightlake Coverage</span>
    </div>

    <div class="memberships">
      <svg class="badge badge-bepwo" width="56" height="34" viewBox="0 0 56 34" role="img" aria-label="BEPWO membership badge">
        <polygon points="28,2 50,30 6,30" fill="var(--brand-blue)"/>
      </svg>
      <svg class="badge badge-gqlf" width="40" height="40" viewBox="0 0 40 40" role="img" aria-label="GQLF membership badge">
        <circle cx="20" cy="20" r="17" fill="none" stroke="var(--brand-blue)" stroke-width="4"/>
      </svg>
    </div>

    <div class="person">
      <p class="person-name">Owen R. Tessler</p>
      <p class="person-title">President</p>
    </div>

    <div class="contact-band">
      <p class="contact-address">4620 W. Hollister Rd, Suite 310, Maple Ridge, CO 80999</p>
      <p class="contact-phone">(555) 555-0147</p>
      <p class="contact-email">owen@brightlakecoverage.com</p>
    </div>

    <p class="tagline-strip">Your resource for life, long term care, and disability insurance</p>
  </section>

</main>
</body>
</html>
```